New Basketball Sports Agency need webpage design

We are a GRVO/PKL Sports agency looking for a new Webpage design. We currently have a site @ www.tqrhoopsgroup.example, and looking for someone to redesign the site.. We are also looking to redo the LOGO as well. TQR will begin its Vantage clinics also, and would like a page to promote and sign up for camp. I already have quidlane, but not sure how to add to site. Site must include:

Page for Agency updates, Client profiles, page for admin, camp registration page, flash photos, and able to filter news updates from contihoops, and KWVR sites.
Updates

Target Market(s)

European basketball clubs, USA Teams, Basketball Players, Sports Agents, Sports Directors General Managers,

Industry/Entity Type

News

```html
<!DOCTYPE html>
<html lang="en">
<head>
<meta charset="utf-8">
<title>TQR – Tri-Quarter Sports Management</title>
<link rel="stylesheet" href="https://fonts.googleapis.com/css2?family=Cormorant+Garamond:wght@500&family=Noto+Serif:wght@400;700&family=Arimo:wght@400&display=swap">
<style>
:root{
  --ink-dark:#141416;
  --hero-top:#2a2830;
  --hero-glow:#4a4654;
  --strip:#1c1c1f;
  --paper:#e7e7e7;
  --paper-line:#dcdcdc;
  --copper:#a8652c;
  --copper-deep:#8a4f1f;
  --copper-text:#9a5a24;
  --link-gold:#b8773a;
  --cream:#f6ead9;
  --white:#ffffff;
  --body-text:#222222;
  --rule:#cfcfcf;
}
*{box-sizing:border-box;margin:0;padding:0}
html,body{width:842px;height:1200px;overflow:hidden;background:var(--ink-dark)}
.page{position:relative;width:842px;height:1200px;overflow:hidden;font-family:"Noto Serif",serif}
.abs{position:absolute}

/* header / hero */
.hero{left:0;top:0;width:842px;height:360px;
  background:radial-gradient(ellipse at 55% 25%,var(--hero-glow) 0%,var(--hero-top) 40%,var(--ink-dark) 80%)}
.hero-strip{left:0;top:283px;width:842px;height:77px;background:var(--strip)}
.brand{left:120px;top:12px;display:flex;align-items:center;gap:8px}
.brand-dot{width:50px;height:50px;border-radius:50%;background:var(--copper)}
.brand-name{font-family:"Noto Serif",serif;font-size:32px;color:var(--white);font-weight:400;margin-top:18px}
.utility{right:121px;top:28px;font-size:9px;color:var(--white)}
.utility span{margin:0 6px}
.nav{left:276px;top:63px;display:flex;gap:14px;font-size:11.5px;font-weight:700;color:var(--white);letter-spacing:.2px}
.nav-rule{left:275px;top:78px;width:448px;height:1px;background:#8c8c96}
.hero-title{left:282px;top:124px;font-family:"Cormorant Garamond",serif;font-weight:500;font-size:38px;letter-spacing:.5px;color:var(--white);white-space:nowrap;z-index:2}
.hero-copy{left:282px;top:168px;width:290px;font-size:13.6px;line-height:18px;color:var(--white);white-space:nowrap;z-index:2}
.btn-more{left:285px;top:237px;width:106px;height:21px;border-radius:3px;
  background:linear-gradient(#d6d6d6,#9c9c9c);color:#6b4a2a;font-size:10.5px;font-weight:700;
  text-align:center;line-height:21px}
.player{left:90px;top:150px;width:130px;height:207px;border-radius:40px;
  background:linear-gradient(160deg,#b33030,#6a1b1b)}
.hoop{left:566px;top:188px;width:156px;height:112px;border-radius:14px;z-index:1;
  background:linear-gradient(150deg,#eeeeee,#9b9b9b 70%,#b0642a)}
.hero-tag{left:267px;top:296px;font-size:38px;font-weight:700;color:var(--white);letter-spacing:1px}
.slide-nav{top:348px;width:18px;height:13px;border-radius:2px;background:linear-gradient(#fafafa,#cfcfcf)}

/* welcome */
.welcome{left:0;top:360px;width:842px;height:365px;
  background:repeating-linear-gradient(90deg,var(--paper) 0 3px,var(--paper-line) 3px 4px)}
.shadow-rule{left:125px;width:592px;height:8px;border-radius:50%;
  background:radial-gradient(ellipse at center,rgba(0,0,0,.35),rgba(0,0,0,0) 70%)}
.welcome-title{left:0;top:380px;width:842px;text-align:center;font-size:19.5px;font-weight:700;color:var(--copper-text)}
.col-title{top:436px;font-size:17.5px;font-weight:400;color:var(--copper-text)}
.thumb{left:120px;width:50px;height:64px}
.blurb{font-family:"Arimo",sans-serif;font-size:7.4px;line-height:9.4px;color:var(--body-text)}
.why .blurb{left:178px;width:185px}
.news .blurb{left:445px;width:250px}
.more-link{font-size:7.2px;color:var(--link-gold);letter-spacing:.2px}
.col-divider{left:370px;top:470px;width:1px;height:222px;background:var(--rule)}
.row-divider{left:378px;width:325px;height:1px;background:var(--rule)}
.date{left:385px;width:43px;height:38px;border-radius:6px;background:var(--copper-deep);overflow:hidden;text-align:center}
.date-month{margin:3px 3px 0;height:18px;border-radius:4px 4px 0 0;background:var(--white);color:var(--copper-deep);font-family:"Arimo",sans-serif;font-size:9px;line-height:18px}
.date-day{font-family:"Arimo",sans-serif;font-size:10px;color:var(--white);line-height:15px}

/* awards */
.awards{left:0;top:725px;width:842px;height:200px;
  background:repeating-linear-gradient(135deg,var(--copper) 0 4px,#a4622a 4px 6px)}
.awards-title{left:131px;top:741px;font-size:17px;font-weight:400;color:var(--white)}
.awards-list{left:130px;top:771px;list-style:none;font-size:12.3px;line-height:15.9px;color:var(--cream)}
.awards-list li{display:flex;align-items:center;gap:9px}
.ball{display:inline-block;width:10px;height:10px;border-radius:50%;background:radial-gradient(circle at 35% 35%,#e0703a,#9c3b17)}
.video{left:468px;top:752px;width:231px;height:146px;border:3px solid #111;
  background:linear-gradient(160deg,#2b2b33,#8a2a28 55%,#d9d9d9)}
.play{left:569px;top:812px}

/* footer */
.footer{left:0;top:925px;width:842px;height:275px;background:linear-gradient(120deg,#0b0b0c,#1d1d20 50%,#070707)}
.links-label{left:120px;top:937px;font-size:12px;color:var(--link-gold)}
.group-title{top:963px;display:flex;align-items:center;gap:7px;font-size:12.5px;color:var(--link-gold)}
.link-name{font-size:12px;color:var(--link-gold)}
.link-desc{font-size:9.8px;line-height:13px;color:var(--white)}
.footer-brand{left:606px;top:1110px;display:flex;align-items:center;gap:7px}
.footer-brand .brand-dot{width:48px;height:48px}
.footer-brand .brand-name{font-size:30px;margin-top:16px}
.copyright{left:460px;top:1184px;width:240px;text-align:right;white-space:nowrap;font-family:"Arimo",sans-serif;font-size:8px;color:var(--white)}
</style>
</head>
<body>
<div class="page">

  <header>
    <div class="abs hero"></div>
    <div class="abs hero-strip"></div>
    <div class="abs brand"><span class="brand-dot"></span><span class="brand-name">TQR</span></div>
    <div class="abs utility">About Us<span>/</span>Contact Us &nbsp;+001-555-0142</div>
    <nav class="abs nav"><span>HOME</span><span>CLINTS</span><span>BASKETBALL BOOTCAMP</span><span>HIGH SCHOOL SERVICES</span><span>MORE...</span></nav>
    <div class="abs nav-rule"></div>
  </header>

  <section class="hero-slide">
    <div class="abs player" role="img" aria-label="Photo cut-out of a player dribbling a basketball"></div>
    <div class="abs hoop" role="img" aria-label="Photo of a basketball dropping through a hoop and backboard"></div>
    <h1 class="abs hero-title">New Member Trial Sessions</h1>
    <p class="abs hero-copy">Think you have what it takes to make the<br>team? Come down and find out. Play some<br>basketball and have fun.</p>
    <div class="abs btn-more">READ MORE</div>
    <div class="abs hero-tag">WORLD WIDE</div>
    <svg class="abs slide-nav" style="left:653px" viewBox="0 0 18 13"><path d="M10 4 L7 6.5 L10 9" fill="none" stroke="#333" stroke-width="1.3"/></svg>
    <svg class="abs slide-nav" style="left:673px" viewBox="0 0 18 13"><path d="M8 4 L11 6.5 L8 9" fill="none" stroke="#333" stroke-width="1.3"/></svg>
  </section>

  <section>
    <div class="abs welcome"></div>
    <div class="abs shadow-rule" style="top:360px"></div>
    <h2 class="abs welcome-title">Welcome to Tri-Quarter Sports Management</h2>
    <div class="abs shadow-rule" style="top:415px"></div>

    <div class="why">
      <h3 class="abs col-title" style="left:120px">Why Join Us</h3>
      <div class="abs thumb" style="top:470px;background:linear-gradient(#4a7ca8,#b5443a)" role="img" aria-label="Photo of a young player seated courtside"></div>
      <p class="abs blurb" style="top:470px">Lorem ipsum dolor sit amet, consectetuer adipiscing elit, sed diam nonummy nibh euismod tincidunt ut laoreet dolore magna aliquam erat volutpat. Ut wisi enim ad minim veniam, quis nostrud exerci tation ullamcorper suscipit lobortis ...</p>
      <span class="abs more-link" style="left:178px;top:526px">READ MORE</span>
      <div class="abs thumb" style="top:559px;background:linear-gradient(#8fa390,#6e5a4c)" role="img" aria-label="Photo of two coaches talking together"></div>
      <p class="abs blurb" style="top:559px">Lorem ipsum dolor sit amet, consectetuer adipiscing elit, sed diam nonummy nibh euismod tincidunt ut laoreet dolore magna aliquam erat volutpat. Ut wisi enim ad minim veniam, quis nostrud exerci tation ullamcorper suscipit lobortis ...</p>
      <span class="abs more-link" style="left:178px;top:615px">READ MORE</span>
      <div class="abs thumb" style="top:647px;background:linear-gradient(#3a3a44,#7d6e8c)" role="img" aria-label="Photo of a player lifting a championship trophy"></div>
      <p class="abs blurb" style="top:647px">Lorem ipsum dolor sit amet, consectetuer adipiscing elit, sed diam nonummy nibh euismod tincidunt ut laoreet dolore magna aliquam erat volutpat. Ut wisi enim ad minim veniam, quis nostrud exerci tation ullamcorper suscipit lobortis ...</p>
      <span class="abs more-link" style="left:178px;top:703px">READ MORE</span>
    </div>

    <div class="abs col-divider"></div>

    <div class="news">
      <h3 class="abs col-title" style="left:378px">Latest News</h3>
      <div class="abs date" style="top:470px"><div class="date-month">JUNE</div><div class="date-day">25</div></div>
      <p class="abs blurb" style="top:470px">Lorem ipsum dolor sit amet, consectetuer adipiscing elit, sed diam nonummy nibh euismod tincidunt ut laoreet dolore magna aliquam erat volutpat. Ut wisi enim ad minim veniam, quis nostrud exerci tation ullamcorper suscipit lobortis ...</p>
      <span class="abs more-link" style="left:445px;top:527px">READ MORE</span>
      <div class="abs row-divider" style="top:547px"></div>
      <div class="abs date" style="top:559px"><div class="date-month">JUNE</div><div class="date-day">24</div></div>
      <p class="abs blurb" style="top:559px">Lorem ipsum dolor sit amet, consectetuer adipiscing elit, sed diam nonummy nibh euismod tincidunt ut laoreet dolore magna aliquam erat volutpat. Ut wisi enim ad minim veniam, quis nostrud exerci tation ullamcorper suscipit lobortis ...</p>
      <span class="abs more-link" style="left:445px;top:615px">READ MORE</span>
      <div class="abs row-divider" style="top:636px"></div>
      <div class="abs date" style="top:647px"><div class="date-month">JUNE</div><div class="date-day">23</div></div>
      <p class="abs blurb" style="top:647px">Lorem ipsum dolor sit amet, consectetuer adipiscing elit, sed diam nonummy nibh euismod tincidunt ut laoreet dolore magna aliquam erat volutpat. Ut wisi enim ad minim veniam, quis nostrud exerci tation ullamcorper suscipit lobortis ...</p>
      <span class="abs more-link" style="left:445px;top:703px">READ MORE</span>
    </div>
  </section>

  <section>
    <div class="abs awards"></div>
    <h3 class="abs awards-title">Awards/Achievements:</h3>
    <ul class="abs awards-list">
      <li><span class="ball"></span>2010-1st Team All Region</li>
      <li><span class="ball"></span>2010-All-American</li>
      <li><span class="ball"></span>2010- Jucco Top 100-All-American</li>
      <li><span class="ball"></span>2011- Preseason All-American</li>
      <li><span class="ball"></span>2012- Nation Top Free-Throw % (96.1)</li>
      <li><span class="ball"></span>2012-All –RPC Honorable Mention</li>
      <li><span class="ball"></span>2013- All MVAC Honorable Mention</li>
      <li><span class="ball"></span>2013- Scored over 2,000 career points</li>
    </ul>
    <div class="abs video" role="img" aria-label="Video still of a player shooting a jump shot in a gym"></div>
    <svg class="abs play" width="28" height="28" viewBox="0 0 28 28"><circle cx="14" cy="14" r="13" fill="rgba(0,0,0,.35)" stroke="#fff" stroke-width="1.5"/><path d="M11 8 L20 14 L11 20 Z" fill="#fff"/></svg>
  </section>

  <footer>
    <div class="abs footer"></div>
    <div class="abs links-label">LINKS</div>

    <div class="abs group-title" style="left:122px"><span class="ball"></span>PRO BASKETBALL</div>
    <div class="abs link-name" style="left:143px;top:987px">PKL</div>
    <div class="abs link-desc" style="left:141px;top:1005px">League, Team, Player info...</div>
    <div class="abs link-name" style="left:143px;top:1034px">PKL-D</div>
    <div class="abs link-desc" style="left:143px;top:1051px">PKL Developmental League</div>
    <div class="abs link-name" style="left:143px;top:1081px">UHA</div>
    <div class="abs link-desc" style="left:143px;top:1098px">Unified Hoops Alliance<br>“More Than Just a League”</div>
    <div class="abs link-name" style="left:143px;top:1140px">GRVO</div>
    <div class="abs link-desc" style="left:143px;top:1156px">International Basketball<br>AGENTS/ PLAYERS</div>

    <div class="abs group-title" style="left:334px"><span class="ball"></span>CIAB BASKETBALL</div>
    <div class="abs link-name" style="left:354px;top:988px">CIAB</div>
    <div class="abs link-desc" style="left:353px;top:1006px">League, Team, Player info...</div>
    <div class="abs link-name" style="left:354px;top:1034px">CIAB ELIGIBILITY CENTER</div>
    <div class="abs link-desc" style="left:355px;top:1051px">PKL Developmental League</div>

    <div class="abs group-title" style="left:551px"><span class="ball"></span>MISC BASKETBALL</div>
    <div class="abs link-name" style="left:570px;top:989px">HoopLine</div>
    <div class="abs link-desc" style="left:570px;top:1004px">League, Team, Player info...</div>
    <div class="abs link-name" style="left:570px;top:1035px">VERT JOURNAL</div>
    <div class="abs link-desc" style="left:571px;top:1051px">PKL Developmental League</div>
    <div class="abs link-name" style="left:567px;top:1084px">CONTIHOOPS</div>

    <div class="abs footer-brand"><span class="brand-dot"></span><span class="brand-name">TQR</span></div>
    <div class="abs copyright">© 2013 tqrbasketball.example. All rights reserved.</div>
  </footer>

</div>
</body>
</html>
```